依頼詳細
新設法人による新規名刺作成です。
一般顧客が主ですので、基本はシンプルで分かり易いデザインがいいかと思いますが、特にこだわりません。
私がいいと思っている一例の画像添付しますが、他に良い案あればご提案ください。
記載項目
【会社情報】
社名)コトノ・ヴェール株式会社
氏名)高瀬 航平
役職)代表取締役
資格)宅地建物取引士、一級建築士
住所)奈良県橿原市柳原町204-3-1
TEL)0744-61-9472
FAX)0744-61-9473
MAIL)kotonovale@mail.tsumikinet.jp

【許可情報】
建設業許可)奈良県知事(般-05)第04872号
宅建免許)奈良県知事(2)第0456号

【業務内容】※レイアウトのバランス悪ければ記載不要
・住宅/店舗/事務所等 各種施設施工
・リフォーム
・分譲住宅販売
・土地建物 仲介/賃貸/売買/利活用

希望イメージ
シンプル 複雑
単色 カラフル
暗い 明るい
日常 高級
遊び心 厳粛
未来的 伝統的
女性的 男性的
希望する色
納品ファイル
• 高解像度JPG (.jpg)
• イラストレーター形式 (.ai)
• フォトショップ形式 (.psd)
• PNG形式 (.png)
補足説明
許可番号や氏名等、随時変更しますので、編集しやすいデータ形式で納品お願いします。
■ 選んだ理由

最終的な決め手はデザイン力であったと思います。
限られてレイアウトの中で、良い提案をしていただきました。

■ 提案者全員のお礼・コメント

たくさんの良い提案ありがとうございます。
またこちらのお願いも快く引き受けていただき感謝申し上げます。

今回ご縁ございませんでしたが、また機会ございましたら宜しくお願い致します。

```html
<!DOCTYPE html>
<html lang="ja">
<head>
<meta charset="utf-8">
<title>コトノ・ヴェール株式会社 名刺</title>
<link rel="stylesheet" href="https://fonts.googleapis.com/css2?family=Noto+Sans+JP:wght@400;500;700&family=Montserrat:wght@600;700&display=swap">
<style>
  :root {
    --board: #e4e4e4;
    --label: #555555;
    --card: #ffffff;
    --ink: #222222;
    --ink-soft: #444444;
    --blue: #2e97e0;
    --blue-light: #6fc2f2;
    --navy: #1c3f98;
    --white: #ffffff;
  }
  * { margin: 0; padding: 0; box-sizing: border-box; }
  html, body { width: 805px; height: 1200px; overflow: hidden; }
  body {
    position: relative;
    background: var(--board);
    font-family: "Noto Sans JP", sans-serif;
    color: var(--ink);
  }
  .side-label {
    position: absolute;
    left: 40px;
    font-family: "Montserrat", sans-serif;
    font-weight: 600;
    font-size: 17px;
    color: var(--label);
  }
  .side-label.front { top: 72px; }
  .side-label.back { top: 626px; }

  .card {
    position: absolute;
    left: 38px;
    width: 729px;
    height: 435px;
    overflow: hidden;
    box-shadow: 0 3px 10px rgba(0,0,0,0.22);
  }
  .card.front { top: 118px; background: var(--card); }
  .card.back { top: 672px; background: var(--blue); }

  .corner { position: absolute; }
  .corner.top-right { right: 0; top: 0; }
  .corner.bottom-left { left: 0; bottom: 0; }

  .brand {
    position: absolute;
    display: flex;
    align-items: center;
    font-family: "Montserrat", sans-serif;
    font-weight: 700;
    white-space: nowrap;
  }
  .card.front .brand {
    left: 40px; top: 50px; width: 176px;
    flex-direction: column;
    gap: 8px;
    font-size: 25px;
    line-height: 30px;
    color: var(--navy);
  }
  .brand-mark { display: block; background: var(--blue); }
  .card.front .brand-mark { width: 40px; height: 40px; }
  .card.back .brand {
    left: 0; right: 0; top: 140px;
    justify-content: center;
    font-size: 44px;
    color: var(--white);
    gap: 16px;
  }
  .card.back .brand-mark { width: 30px; height: 30px; background: var(--white); }

  .profile { position: absolute; left: 232px; top: 58px; }
  .role { font-size: 13px; color: var(--ink-soft); }
  .name-row { display: flex; align-items: baseline; gap: 14px; margin-top: 2px; }
  .name { font-size: 32px; font-weight: 700; letter-spacing: 2px; }
  .name-roman { font-size: 13px; color: var(--ink-soft); }
  .rule { width: 300px; height: 1px; background: #999; margin: 4px 0 6px; }
  .license-title { font-size: 13px; color: var(--ink-soft); }

  .company { position: absolute; left: 232px; top: 188px; }
  .company-name { font-size: 17px; font-weight: 700; margin-bottom: 6px; }
  .contact-row {
    display: flex; align-items: center; gap: 6px;
    font-size: 13.5px; line-height: 24px; color: var(--ink);
  }
  .icon {
    display: inline-flex; align-items: center; justify-content: center;
    width: 18px; height: 18px; background: var(--navy); border-radius: 2px;
  }
  .contact-row .gap { width: 12px; }
  .permits { margin-top: 4px; font-size: 11.5px; line-height: 18px; color: var(--ink-soft); }

  .services {
    position: absolute; left: 0; right: 0; bottom: 0; height: 88px;
    background: var(--navy);
    color: var(--white);
    font-size: 13.5px; line-height: 24px;
    padding: 20px 0 0 150px;
  }
</style>
</head>
<body>

<p class="side-label front">Front</p>
<section class="card front" aria-label="名刺 表面">
  <svg class="corner top-right" width="140" height="150" viewBox="0 0 140 150" aria-hidden="true">
    <polygon points="0,0 140,0 140,150" fill="var(--blue)"/>
    <polygon points="50,0 140,0 140,95" fill="var(--navy)"/>
    <polygon points="0,0 60,0 90,60" fill="var(--blue-light)"/>
  </svg>
  <svg class="corner bottom-left" width="130" height="110" viewBox="0 0 130 110" aria-hidden="true">
    <polygon points="0,0 0,110 130,110" fill="var(--blue)"/>
    <polygon points="0,40 0,110 90,110" fill="var(--navy)"/>
    <polygon points="40,110 130,110 110,70" fill="var(--blue-light)"/>
  </svg>

  <div class="brand"><span class="brand-mark"></span>kotono vale</div>

  <div class="profile">
    <p class="role">代表取締役</p>
    <div class="name-row">
      <span class="name">高瀬 航平</span>
      <span class="name-roman">Kohei Takase</span>
    </div>
    <div class="rule"></div>
    <p class="license-title">宅地建物取引士／一級建築士</p>
  </div>

  <div class="company">
    <p class="company-name">コトノ・ヴェール株式会社</p>
    <p class="contact-row">
      <span class="icon"><svg width="12" height="12" viewBox="0 0 12 12"><path d="M6 1 L11 5.5 H9.5 V11 H2.5 V5.5 H1 Z" fill="#fff"/></svg></span>
      〒634-0007 奈良県橿原市柳原町204-3-1
    </p>
    <p class="contact-row">
      <span class="icon"><svg width="12" height="12" viewBox="0 0 12 12"><path d="M3 1.5 L5 1.5 L5.6 4 L4.3 5 Q5.3 7 7 7.8 L8 6.5 L10.5 7.1 L10.5 9.3 Q10 10.5 8.6 10.5 Q2 9.6 1.5 3 Q1.6 1.6 3 1.5 Z" fill="#fff"/></svg></span>
      0744-61-9472
      <span class="gap"></span>
      <span class="icon"><svg width="12" height="12" viewBox="0 0 12 12"><rect x="2" y="1.5" width="8" height="3" fill="#fff"/><rect x="1" y="5" width="10" height="4.5" fill="#fff"/><rect x="3" y="8" width="6" height="3" fill="#fff"/></svg></span>
      0744-61-9473
    </p>
    <p class="contact-row">
      <span class="icon"><svg width="12" height="12" viewBox="0 0 12 12"><rect x="1" y="2.5" width="10" height="7" fill="#fff"/><path d="M1 2.5 L6 6.5 L11 2.5" stroke="var(--navy)" stroke-width="1" fill="none"/></svg></span>
      kotonovale@mail.tsumikinet.jp
    </p>
    <div class="permits">
      <p>建設業許可：奈良県知事(般-05)第04872号</p>
      <p>宅建免許：奈良県知事(2)第0456号</p>
    </div>
  </div>
</section>

<p class="side-label back">Back</p>
<section class="card back" aria-label="名刺 裏面">
  <div class="brand"><span class="brand-mark"></span>kotono vale</div>
  <div class="services">
    <p>● 住宅・店舗・事務所等／各種施設施工　● リフォーム　● 分譲住宅販売</p>
    <p>● 土地建物／仲介・賃貸・売買・利活用</p>
  </div>
</section>

</body>
</html>
```